Hockey Sponsorship Proposal

We are looking for a sponsorship proposal design for an apparel company to supply our hockey camps with jerseys and apparel. We want to use lots of visuals so potential business partners can see the exposure and publicity their company could get by working with us. We would like the primary colors to be red, black and white. We have attached a bunch of images but not all need to be used. We would like to see a mix of images with adult players and youth players where appropriate. Although I have provided a rough outline for the information on the powerpoint the text and images can be displayed however you would like.

Here is a link to some proposals to give you an idea of what we are looking for
https://www.quillrack.co.uk/pin/512604837219056471/

Target Market(s)

Athletic Apparel Companies

Industry/Entity Type

It Company

Requirements
Must have
• Please note this should be suitable for web as the proposal will be emailed. This is NOT for print.
Nice to have
• I would like the first page to have a full image as the backdrop with the text over top if possible.

```html
<!DOCTYPE html>
<html lang="en">
<head>
<meta charset="utf-8">
<title>Service Requirements</title>
<link href="https://fonts.googleapis.com/css2?family=Oswald:wght@400;500;600&display=swap" rel="stylesheet">
<style>
  :root {
    --stage: #cfcfcf;
    --navy: #1e2a50;
    --white: #ffffff;
    --row-light: rgba(255,255,255,0.88);
    --row-shade: rgba(196,201,216,0.92);
    --ink: #151a2c;
    --photo-warm: #e8e3dc;
    --photo-cool: #eef0f0;
  }
  * { margin: 0; padding: 0; box-sizing: border-box; }
  html, body { width: 1200px; height: 1000px; overflow: hidden; background: var(--stage); }
  body { position: relative; font-family: "Oswald", "Arial Narrow", sans-serif; }

  .slide {
    position: absolute; left: 35px; top: 125px; width: 1130px; height: 750px;
    overflow: hidden; background: var(--photo-cool);
  }
  .backdrop-photo {
    position: absolute; inset: 0;
    background: linear-gradient(180deg, var(--photo-cool) 0%, var(--photo-warm) 30%, #efe3e0 55%, #e9e6e2 100%);
  }
  .title-banner { position: absolute; left: 0; top: 67px; width: 1100px; height: 85px; }
  .title {
    position: absolute; left: 102px; top: 68px;
    color: var(--white); font-size: 62px; font-weight: 600; letter-spacing: 0.5px; line-height: 84px;
  }

  .requirements { position: absolute; left: 0; top: 228px; width: 1130px; }
  .req-head {
    height: 50px; background: var(--navy); color: var(--white);
    display: grid; grid-template-columns: 245px 460px 210px 215px;
    align-items: center; font-size: 23px; font-weight: 500;
  }
  .req-head span { text-align: center; }
  .req-head .col-event { text-align: left; padding-left: 95px; }
  .req-head .col-item { padding-left: 50px; }
  .req-head .col-pieces { text-align: left; padding-left: 130px; }
  .req-head .col-time { text-align: left; padding-left: 37px; }

  .req-row {
    display: grid; grid-template-columns: 318px 450px 145px 217px;
    align-items: center; font-size: 16px; color: var(--ink);
  }
  .req-row:nth-child(odd) { background: var(--row-light); }
  .req-row:nth-child(even) { background: var(--row-shade); }
  .req-row span:first-child { padding-left: 75px; }
  .req-row .pieces { text-align: center; }
  .req-row .timeline { padding-left: 38px; }
  .r1 { height: 40px; padding-top: 8px; }
  .r2 { height: 29px; }
  .r3 { height: 33px; }
  .r4 { height: 33px; }
  .r5 { height: 33px; }
  .r6 { height: 29px; }
  .r7 { height: 42px; padding-bottom: 8px; }

  .photo-strip { position: absolute; left: 0; top: 545px; width: 1130px; height: 205px; }
</style>
</head>
<body>
  <main class="slide">
    <div class="backdrop-photo" role="img" aria-label="Faded photo of a hockey locker room with named stalls and hanging jerseys"></div>

    <svg class="title-banner" viewBox="0 0 1100 85" aria-hidden="true">
      <polygon points="40,0 1100,0 1030,85 0,85" fill="var(--navy)"/>
    </svg>
    <h1 class="title">SERVICE REQUIREMENTS</h1>

    <section class="requirements">
      <div class="req-head">
        <span class="col-event">EVENT</span>
        <span class="col-item">ITEM</span>
        <span class="col-pieces">PIECES</span>
        <span class="col-time">TIMELINE</span>
      </div>
      <div class="req-rows">
        <div class="req-row r1"><span>Pro League Camp</span><span>Uniform &nbsp;(jersey/sock/pant shell)</span><span class="pieces">50</span><span class="timeline">Summer 2018</span></div>
        <div class="req-row r2"><span>Pro League Camp</span><span>Apparel &nbsp;(some of t-shirt, shorts, hoodie, track suit, hat, toque)</span><span class="pieces">50</span><span class="timeline">Summer 2018</span></div>
        <div class="req-row r3"><span>Steeple Super 64</span><span>Uniform &nbsp;(jersey/sock/pant shell)</span><span class="pieces">400</span><span class="timeline">Spring 2018</span></div>
        <div class="req-row r4"><span>Steeple Super 64</span><span>Apparel &nbsp;(some of t-shirt, shorts, hoodie, track suit, hat, toque)</span><span class="pieces">400</span><span class="timeline">Spring 2018</span></div>
        <div class="req-row r5"><span>Steeple Festival</span><span>Uniform &nbsp;(jersey/sock/pant shell)</span><span class="pieces">400</span><span class="timeline">Spring 2018</span></div>
        <div class="req-row r6"><span>Steeple Festival</span><span>Apparel (some of t-shirt, shorts, hoodie, track suit, hat, toque)</span><span class="pieces">400</span><span class="timeline">Spring 2018</span></div>
        <div class="req-row r7"><span>Travel Team</span><span>Uniform &nbsp;(jersey/sock/pant shell)</span><span class="pieces">20</span><span class="timeline">Fall 2018</span></div>
      </div>
    </section>

    <svg class="photo-strip" viewBox="0 0 1130 205">
      <defs>
        <linearGradient id="rink-a" x1="0" y1="0" x2="0" y2="1">
          <stop offset="0" stop-color="#b9c2bd"/><stop offset="0.55" stop-color="#a7332f"/><stop offset="1" stop-color="#e4e6ea"/>
        </linearGradient>
        <linearGradient id="rink-b" x1="0" y1="0" x2="0" y2="1">
          <stop offset="0" stop-color="#c9a879"/><stop offset="0.6" stop-color="#3b3f55"/><stop offset="1" stop-color="#2f4f9a"/>
        </linearGradient>
        <linearGradient id="rink-c" x1="0" y1="0" x2="0" y2="1">
          <stop offset="0" stop-color="#c4c6bf"/><stop offset="0.5" stop-color="#8f9097"/><stop offset="1" stop-color="#f1f2f4"/>
        </linearGradient>
        <linearGradient id="rink-d" x1="0" y1="0" x2="0" y2="1">
          <stop offset="0" stop-color="#b8c0c6"/><stop offset="0.55" stop-color="#b9383a"/><stop offset="1" stop-color="#e9e9ec"/>
        </linearGradient>
      </defs>
      <rect x="0" y="0" width="1130" height="205" fill="var(--navy)"/>
      <polygon points="83,30 355,30 295,205 25,205" fill="url(#rink-a)" role="img" aria-label="Photo of youth players in red jerseys on the ice"/>
      <polygon points="355,30 595,30 540,205 295,205" fill="url(#rink-b)" role="img" aria-label="Photo of a coach reviewing video with players"/>
      <polygon points="595,30 840,30 785,205 540,205" fill="url(#rink-c)" role="img" aria-label="Photo of a coach leading a drill on the rink"/>
      <polygon points="840,30 1105,30 1045,205 785,205" fill="url(#rink-d)" role="img" aria-label="Photo of players and a coach at the bench"/>
      <polygon points="83,30 100,30 42,205 25,205" fill="var(--white)"/>
      <polygon points="345,30 360,30 300,205 285,205" fill="var(--white)"/>
      <polygon points="588,30 600,30 545,205 533,205" fill="var(--white)"/>
      <polygon points="833,30 845,30 790,205 778,205" fill="var(--white)"/>
      <polygon points="1090,30 1105,30 1045,205 1030,205" fill="var(--white)"/>
    </svg>
  </main>
</body>
</html>
```